stationary
envelopes, letterhead, biz card
I need single sided standard sized Business Card [3.5" x 2"]
doesnt matter whatever looks good
Professional
Marten Olufsson
President
4218 Wexhollow Ave Ste 202-517
marten@bexlin.com
www.bexlin.com

```html
<!DOCTYPE html>
<html lang="en">
<head>
<meta charset="utf-8">
<title>Bexlin Business Card</title>
<link href="https://fonts.googleapis.com/css2?family=Questrial&family=Open+Sans:ital,wght@0,700;1,700&display=swap" rel="stylesheet">
<style>
  :root {
    --bg: #2a2a2c;
    --brand-blue: #1fa3dc;
    --brand-blue-dark: #1589bd;
    --ink: #3a3a3c;
    --ink-soft: #6d6d70;
    --paper: #ffffff;
    --paper-shade: #eef0f2;
  }
  * { margin: 0; padding: 0; box-sizing: border-box; }
  html, body { width: 1200px; height: 901px; overflow: hidden; }
  body {
    background: var(--bg);
    font-family: "Questrial", "Helvetica Neue", sans-serif;
    position: relative;
  }
  .card {
    position: absolute;
    left: 250px;
    width: 700px;
    height: 400px;
    border-radius: 6px;
    overflow: hidden;
    box-shadow: 0 12px 30px rgba(0,0,0,0.45);
  }
  /* back face */
  .card-back {
    top: 35px;
    background: linear-gradient(135deg, #36b6ea 0%, var(--brand-blue) 55%, var(--brand-blue-dark) 100%);
  }
  .card-back .brand-mark {
    position: absolute;
    top: 150px; left: 0; right: 0;
    display: flex; align-items: center; justify-content: center; gap: 18px;
    color: var(--paper);
    font-size: 64px;
    letter-spacing: 2px;
  }
  .brand-square {
    width: 34px; height: 34px;
    background: currentColor;
  }
  .card-back .back-url {
    position: absolute;
    left: 0; right: 0; bottom: 70px;
    text-align: center;
    color: var(--paper);
    font-size: 20px;
    letter-spacing: 1px;
  }
  /* front face */
  .card-front {
    top: 466px;
    background: linear-gradient(160deg, var(--paper) 0%, var(--paper) 60%, var(--paper-shade) 100%);
  }
  .edge-tab {
    position: absolute;
    width: 14px;
    background: var(--brand-blue);
  }
  .edge-tab.left { left: 0; top: 250px; height: 100px; border-radius: 0 8px 8px 0; }
  .edge-tab.right { right: 0; top: 55px; height: 90px; border-radius: 8px 0 0 8px; }
  .front-brand {
    position: absolute;
    left: 48px; top: 70px;
    display: flex; align-items: center; gap: 12px;
    color: var(--ink);
    font-size: 52px;
    letter-spacing: 1px;
  }
  .front-brand .brand-square { width: 28px; height: 28px; color: var(--brand-blue); }
  .address {
    position: absolute;
    left: 48px; top: 150px;
    color: var(--ink);
    font-size: 17px;
    line-height: 1.3;
  }
  .contacts {
    position: absolute;
    left: 48px; top: 218px;
    list-style: none;
  }
  .contacts li {
    display: flex; align-items: center; gap: 10px;
    color: var(--ink);
    font-size: 18px;
    height: 32px;
  }
  .contacts svg { width: 18px; height: 18px; flex: none; }
  .person {
    position: absolute;
    right: 40px; top: 66px;
    text-align: right;
    font-family: "Open Sans", Arial, sans-serif;
    font-weight: 700;
  }
  .person .name { color: var(--brand-blue); font-size: 24px; font-style: italic; }
  .person .title { color: var(--ink); font-size: 16px; margin-top: 2px; }
</style>
</head>
<body>
  <section class="card card-back" aria-label="Card back">
    <div class="brand-mark"><span class="brand-square"></span><span>Bexlin</span></div>
    <div class="back-url">www.bexlin.com</div>
  </section>

  <section class="card card-front" aria-label="Card front">
    <span class="edge-tab left"></span>
    <span class="edge-tab right"></span>

    <div class="front-brand"><span class="brand-square"></span><span>Bexlin</span></div>

    <p class="address">4218 Wexhollow<br>Ave Ste 202-517</p>

    <ul class="contacts">
      <li>
        <svg viewBox="0 0 18 18"><circle cx="9" cy="9" r="9" fill="var(--brand-blue)"/><path d="M6 4.5l1.8 0 .8 2.4-1.1.9a6 6 0 0 0 2.7 2.7l.9-1.1 2.4.8v1.8c0 .5-.4.9-1 .9A8 8 0 0 1 5.1 5.5c0-.6.4-1 .9-1z" fill="#fff"/></svg>
        <span>555.418.2290</span>
      </li>
      <li>
        <svg viewBox="0 0 18 18"><circle cx="9" cy="9" r="9" fill="var(--brand-blue)"/><rect x="4" y="6" width="10" height="7" rx="1" fill="#fff"/><rect x="6" y="4" width="6" height="3" fill="#fff"/></svg>
        <span>555.730.6614</span>
      </li>
      <li>
        <svg viewBox="0 0 18 18"><circle cx="9" cy="9" r="9" fill="var(--brand-blue)"/><rect x="4" y="5.5" width="10" height="7" rx="1" fill="#fff"/><path d="M4.5 6l4.5 3.5L13.5 6" stroke="var(--brand-blue)" stroke-width="1" fill="none"/></svg>
        <span>marten@bexlin.com</span>
      </li>
      <li>
        <svg viewBox="0 0 18 18"><circle cx="9" cy="9" r="9" fill="var(--brand-blue)"/><circle cx="9" cy="9" r="5" fill="none" stroke="#fff" stroke-width="1.2"/><path d="M4 9h10M9 4c-2.5 3-2.5 7 0 10M9 4c2.5 3 2.5 7 0 10" stroke="#fff" stroke-width="1" fill="none"/></svg>
        <span>www.bexlin.com</span>
      </li>
    </ul>

    <div class="person">
      <div class="name">Marten Olufsson</div>
      <div class="title">President</div>
    </div>
  </section>
</body>
</html>
```